Webdesign für Management Coaching
Zielgruppe
Ich bin Coach/biete Coaching-Leistungen an.
Zielgruppe: Fokus auf Führungskräfte/Entscheider/Management mit technischem Hintergrund (Forschung & Entwicklung, Engineering, Technik, Maschinenbau, Naturwissenschaften)
Coaching-Schwerpunkte: Sinn-Coaching, Begleitung bei Umbrüchen und Veränderungen (privat & beruflich), Sparring & Reflexion
Aufgabenstellung
Gewünscht wurde ein helles Design, das die Logo-Farben aufnimmt. Ausrichtung am Logo & den verwendeten Farben, Schriften
Bilder: Ich werde noch Fotos beim Fotografen machen, die eingebunden werden sollen (Profil, etc.). Bitte Anhaltspunkte nennen, worauf ich die Fotografin hinweisen soll/welche Motive ins Konzept passen.

```html
<!DOCTYPE html>
<html lang="de">
<head>
<meta charset="utf-8">
<title>Stefan Brandauer – Klarwerk Coaching</title>
<link href="https://fonts.googleapis.com/css2?family=Playfair+Display:wght@500;600;700&family=EB+Garamond:wght@400;500;600&family=Great+Vibes&family=Montserrat:wght@400;500;600&display=swap" rel="stylesheet">
<style>
:root{
  --blue:#7a9eb0;
  --blue-dark:#5f8598;
  --blue-text:#6f95a8;
  --orange:#ef9444;
  --ink:#2f3b44;
  --hero-bg:#f4f6f9;
  --white:#ffffff;
  --line:#e3e7eb;
}
*{box-sizing:border-box;margin:0;padding:0}
html,body{width:1200px;height:4982px;overflow:hidden}
body{position:relative;font-family:"EB Garamond",serif;color:var(--ink);background:var(--white)}
.abs{position:absolute}
.serif{font-family:"Playfair Display",serif}
.script{font-family:"Great Vibes",cursive;font-weight:400}
.sans{font-family:"Montserrat",sans-serif}
.eyebrow{position:absolute;font-family:"EB Garamond",serif;font-size:14px;letter-spacing:3.5px;text-transform:uppercase;font-weight:500}
.btn{position:absolute;display:flex;align-items:center;justify-content:center;font-family:"Montserrat",sans-serif;font-size:16px;border-radius:3px;height:44px}
.btn-orange{background:var(--orange);color:var(--white)}
.btn-outline{border:1.5px solid var(--blue);color:var(--blue)}
.photo{position:absolute}

/* hero */
.hero{position:absolute;left:0;top:0;width:1200px;height:763px;background:var(--hero-bg);overflow:hidden}
.hero-glow{position:absolute;left:560px;top:300px;width:700px;height:463px;background:linear-gradient(160deg,rgba(244,246,249,0) 35%,#f2c79e 75%,#e9964f 100%)}
.nav{position:absolute;left:100px;top:112px;display:flex;gap:18px;font-family:"Montserrat",sans-serif;font-size:21px;color:var(--blue-dark)}
.brand{position:absolute;left:500px;top:50px;width:200px;text-align:center}
.brand-circle{width:136px;height:136px;border-radius:50%;border:1.5px solid var(--blue);margin:0 auto 14px}
.brand-name{font-family:"EB Garamond",serif;font-size:15px;letter-spacing:2px;color:var(--blue-dark)}
.social{position:absolute;top:110px;width:30px;height:30px;border-radius:50%;border:2.5px solid var(--blue)}
.hero h1{position:absolute;left:100px;top:322px;font-family:"Playfair Display",serif;font-weight:600;font-size:52px;color:var(--blue-dark);line-height:1.1}
.hero h1 .script{font-size:78px;color:var(--blue-dark)}
.hero-text{position:absolute;left:100px;top:490px;width:580px;font-size:16px;line-height:23px}

/* about */
.about h2,.contact h2{position:absolute;font-family:"Playfair Display",serif;font-weight:600;font-size:46px;line-height:64px;color:var(--blue-text)}
.script-blue{font-family:"Great Vibes",cursive;font-weight:400;color:var(--blue-dark)}
.body-text{position:absolute;font-size:15.5px;line-height:23px}
.body-text p+p{margin-top:23px}

/* offer */
.band{position:absolute;left:0;width:1200px;background:var(--blue);color:var(--white)}
.band-title{position:absolute;left:0;width:1200px;text-align:center;font-family:"Playfair Display",serif;font-weight:600;color:var(--white)}
.offer-col{position:absolute;top:250px;width:320px;text-align:center}
.offer-art{width:290px;height:230px;margin:0 auto;border-radius:48% 52% 45% 55%/55% 45% 55% 45%;background:linear-gradient(140deg,#9cb8c6,#8aabbb)}
.offer-col h3{font-family:"Great Vibes",cursive;font-weight:400;font-size:50px;margin-top:18px;line-height:60px}
.offer-col p{font-size:15px;line-height:23px;margin-top:4px}

/* testimonials */
.t-card{position:absolute;left:246px;top:2640px;width:740px;height:370px;border:1px solid var(--line);border-radius:4px;background:var(--white);box-shadow:0 2px 10px rgba(0,0,0,.04)}
.quote{position:absolute;left:70px;top:112px;width:600px;text-align:center;font-family:"Montserrat",sans-serif;font-size:16.5px;letter-spacing:1.6px;line-height:20px;color:var(--ink)}
.dot{position:absolute;top:3044px;width:9px;height:9px;border-radius:50%}

/* blog */
.post{position:absolute;top:334px;width:300px}
.post-img{height:168px}
.post h3{font-family:"Playfair Display",serif;font-weight:700;font-size:25px;line-height:29px;margin-top:22px}
.post p{font-size:15px;line-height:23px;margin-top:16px}

/* footer */
.footer{position:absolute;left:0;top:4807px;width:1200px;height:175px;background:var(--blue);color:var(--white);text-align:center;font-family:"Montserrat",sans-serif}
</style>
</head>
<body>

<!-- Hero -->
<section class="hero">
  <div class="hero-glow"></div>
  <nav class="nav"><span>Home</span><span>Leistungen</span><span>Profil</span><span>Blog</span></nav>
  <div class="brand">
    <div class="brand-circle"></div>
    <div class="brand-name">KLARWERK COACHING</div>
  </div>
  <span class="social" style="left:804px"></span>
  <span class="social" style="left:861px"></span>
  <span class="social" style="left:919px"></span>
  <div class="btn" style="left:983px;top:102px;width:141px;height:42px;background:var(--blue);color:var(--white);font-size:19px">Kontakt</div>

  <div class="eyebrow" style="left:100px;top:292px;color:var(--ink)">Für technische Visionäre</div>
  <h1><span class="script">Coaching,</span><br>das Sie zum <span class="script">Erfolg</span> führt</h1>
  <div class="hero-text">Beratung für Führungskräfte und Entscheider mit technischem Hintergrund.<br>Mit einer fundierten Expertise in den Bereichen Forschung &amp; Entwicklung, Engineering, Technik, Maschinenbau und Naturwissenschaften stehe ich Ihnen zur Seite, um Ihre beruflichen und persönlichen Herausforderungen zu meistern.</div>
  <div class="btn btn-orange" style="left:100px;top:606px;width:272px">Mehr über mein Angebot</div>
  <div class="btn btn-outline" style="left:388px;top:606px;width:222px">Termin vereinbaren</div>

  <div class="photo" role="img" aria-label="Porträtfoto des Coaches mit verschränkten Armen im hellblauen Hemd" style="left:745px;top:270px;width:380px;height:493px;background:linear-gradient(180deg,rgba(190,210,228,.0),rgba(170,196,222,.55) 40%,rgba(150,182,214,.7));border-radius:180px 180px 0 0"></div>
</section>

<!-- About -->
<section class="about">
  <div class="photo" role="img" aria-label="Porträtfoto des Coaches, nachdenklich mit Hand am Kinn" style="left:140px;top:932px;width:330px;height:330px;border-radius:50%;background:linear-gradient(135deg,#cfdbe4,#a9c1d6 55%,#e9eef2)"></div>
  <div class="eyebrow" style="left:535px;top:876px;color:var(--ink)">Stefan Brandauer</div>
  <h2 style="left:535px;top:902px">Profitieren Sie von<br>meiner <span class="script-blue" style="font-size:58px">Expertise</span></h2>
  <div class="body-text" style="left:535px;top:1050px;width:525px">
    <p>Ich bin Stefan Brandauer, zertifizierter Coach mit einer Leidenschaft für die Entwicklung von Führungskräften und Entscheidern im technischen Bereich. Mit einem Hintergrund in [Fachgebiet] und einer langjährigen Erfahrung in der Unterstützung von Menschen auf ihrem Weg zu persönlichem und beruflichem Wachstum, stehe ich Ihnen als vertrauensvoller Begleiter zur Seite.</p>
    <p>Mein Coaching-Ansatz vereint technische Expertise mit einem tiefen Verständnis für persönliche Entwicklung und Sinnhaftigkeit in der Führung. In unserer Zusammenarbeit schaffen wir einen Raum für Reflexion, Sparring und zielgerichtete Veränderung. Meine Mission ist es, Sie dabei zu unterstützen, nicht nur beruflichen Erfolg zu erzielen, sondern auch eine erfüllende und sinnvolle Führungskraft zu werden.</p>
  </div>
  <div class="btn btn-orange" style="left:535px;top:1354px;width:238px;height:42px">Mehr Infos über mich</div>
</section>

<!-- Offer -->
<section class="band" style="top:1511px;height:877px">
  <div class="eyebrow" style="left:0;width:1200px;text-align:center;top:116px">Mein Angebot</div>
  <div class="band-title" style="top:140px;font-size:46px;line-height:80px"><span class="script" style="font-size:62px">Gemeinsam</span> gehen wir auf Kurs</div>
  <div class="offer-col" style="left:102px">
    <div class="offer-art" role="img" aria-label="Illustration: zwei Personen im Gespräch am Tisch"></div>
    <h3>Coaching</h3>
    <p>In meinem Coaching legen wir gemeinsam den Fokus auf bedeutungsvolle Veränderungen in Ihrem Leben und Ihrer beruflichen Laufbahn. Ich unterstütze Sie in den Bereichen Sinn-Coaching, begleite Sie durch Umbrüche und Veränderungen – sei es im privaten oder beruflichen Kontext – und biete Ihnen Sparring und Reflexion auf höchstem Niveau.</p>
  </div>
  <div class="offer-col" style="left:440px">
    <div class="offer-art" role="img" aria-label="Illustration: Zielscheibe mit Pfeil und Person"></div>
    <h3>Ihr Nutzen</h3>
    <p>Als erfahrener Coach verbinde ich Fachkompetenz mit Einfühlungsvermögen, um Ihnen nicht nur praktische Werkzeuge an die Hand zu geben, sondern auch einen Raum für persönliches Wachstum und Entfaltung zu schaffen. Ihr Erfolg und Ihre Zufriedenheit stehen im Mittelpunkt meiner Arbeit.</p>
  </div>
  <div class="offer-col" style="left:780px">
    <div class="offer-art" role="img" aria-label="Illustration: Zahnräder mit Person"></div>
    <h3>Zielgruppe</h3>
    <p>Meine Dienstleistungen richten sich an Führungskräfte und Entscheider in technischen Disziplinen. Ob Sie in der Forschung tätig sind, im Bereich Engineering, Technik, Maschinenbau oder Naturwissenschaften – ich bin hier, um Sie auf Ihrem Weg zu begleiten.</p>
  </div>
</section>

<!-- Testimonials -->
<section class="testimonials">
  <div class="eyebrow" style="left:0;width:1200px;text-align:center;top:2500px;color:var(--ink)">Testimonials</div>
  <div class="abs serif" style="left:0;width:1200px;top:2525px;text-align:center;font-size:50px;font-weight:600;line-height:80px;color:var(--blue-text)"><span style="font-weight:500">Echte</span> Geschichten, echte <span class="script-blue" style="font-size:64px">Erfahrungen</span></div>
  <svg class="abs" style="left:170px;top:2795px" width="36" height="60" viewBox="0 0 36 60"><path d="M28 6 L8 30 L28 54" fill="none" stroke="#e3e7eb" stroke-width="5"/></svg>
  <svg class="abs" style="left:1046px;top:2795px" width="36" height="60" viewBox="0 0 36 60"><path d="M8 6 L28 30 L8 54" fill="none" stroke="#5f6b74" stroke-width="5"/></svg>
  <div class="t-card">
    <svg class="abs" style="left:264px;top:48px" width="250" height="40" viewBox="0 0 250 40">
      <g fill="#ef9444">
        <path id="star" d="M18 2 L22.7 13.5 L35 14.5 L25.6 22.5 L28.5 34.5 L18 28 L7.5 34.5 L10.4 22.5 L1 14.5 L13.3 13.5Z"/>
        <use href="#star" x="53"/><use href="#star" x="106"/><use href="#star" x="159"/><use href="#star" x="212"/>
      </g>
    </svg>
    <div class="quote">"Als technische Führungskraft stand ich vor großen Herausforderungen bei der Umsetzung von Veränderungen in unserem Team. Herr Brandauer hat mir durch sein einfühlsames Coaching geholfen, nicht nur strategische Lösungen zu finden, sondern auch meine persönliche Führungskompetenz zu stärken."</div>
    <div class="photo" role="img" aria-label="Porträtfoto des Kunden" style="left:216px;top:265px;width:70px;height:70px;border-radius:50%;background:linear-gradient(135deg,#d9d9d9,#9a9a9a)"></div>
    <div class="abs sans" style="left:310px;top:277px;font-size:18px;font-weight:600;color:var(--ink)">Lukas Ebner</div>
    <div class="abs sans" style="left:310px;top:304px;font-size:14px;color:#b5bcc2">Nordwerk AG</div>
  </div>
  <span class="dot" style="left:602px;background:#222"></span>
  <span class="dot" style="left:622px;background:#e6e6e6"></span>
  <span class="dot" style="left:642px;background:#e6e6e6"></span>
</section>

<!-- Blog -->
<section class="band" style="top:3168px;height:986px">
  <div class="eyebrow" style="left:0;width:1200px;text-align:center;top:116px">Technik trifft auf Führung</div>
  <div class="band-title script" style="top:150px;font-size:72px;line-height:90px;font-family:'Great Vibes',cursive;font-weight:400">Reflexionen &amp; Erfolgsgeschichten:</div>
  <div class="band-title" style="top:232px;font-size:44px;line-height:60px">Der Coaching-Blog</div>
  <article class="post" style="left:112px">
    <div class="post-img" role="img" aria-label="Foto: Mann in Gedanken am Fenster" style="background:linear-gradient(135deg,#4a4a4a,#c8ccd0 70%,#eef0f2)"></div>
    <h3>Selbstreflexion für Führungskräfte - Kunst und Praxis</h3>
    <p>Tauchen Sie ein in die Kunst der Selbstreflexion und entdecken Sie, warum diese Fähigkeit für technische Führungskräfte so entscheidend ist. Finden Sie praktische Tipps, um diese in Ihren Führungsalltag zu integrieren.</p>
  </article>
  <article class="post" style="left:450px">
    <div class="post-img" role="img" aria-label="Foto: Team bei einem Ideen-Workshop" style="background:linear-gradient(135deg,#c9d9ea,#6f8fb3 60%,#e8d48a)"></div>
    <h3>Innovation und Führung: Kreativität im Management</h3>
    <p>Entdecken Sie, wie Sie Kreativität im technischen Management fördern können: Bewährte Methoden, um eine inspirierende Unternehmenskultur zu schaffen und Innovationen in Ihrem Team zu fördern.</p>
  </article>
  <article class="post" style="left:788px">
    <div class="post-img" role="img" aria-label="Foto: zwei Geschäftsleute im spielerischen Sparring" style="background:linear-gradient(135deg,#5a5f66,#9aa3ab 55%,#b3473d)"></div>
    <h3>Die Macht des Sparrings: Führung per konstruktivem Feedback</h3>
    <p>Erfahren Sie, wie Führungskräfte im technischen Bereich durch Sparring wachsen können. Lesen Sie praktische Einblicke, um Ihre Kompetenzen zu verbessern.</p>
  </article>
  <div class="btn btn-orange" style="left:484px;top:822px;width:230px;height:42px">Alle Artikel anzeigen</div>
</section>

<!-- Contact -->
<section class="contact">
  <div class="eyebrow" style="left:139px;top:4264px;color:var(--ink)">Bereit für Veränderung?</div>
  <h2 style="left:139px;top:4290px;line-height:60px">Ich bin für Sie da.<br><span class="script-blue" style="font-size:64px">Schreiben Sie mir!</span></h2>
  <div class="body-text" style="left:139px;top:4452px;width:480px;font-size:15px;line-height:23px">
    <p>Vereinbaren Sie noch heute Ihr erstes kostenloses Beratungsgespräch und entdecken Sie, wie Coaching Ihr Leben und Ihre berufliche Laufbahn transformieren kann.</p>
    <p>Wenn Sie nach einem engagierten Coach suchen, der Sie in Ihren Zielen unterstützt und Ihnen hilft, Ihr volles Potenzial zu entfalten, nehmen Sie Kontakt auf. Gemeinsam gestalten wir Ihren Weg zu nachhaltigem Erfolg und persönlichem Wohlbefinden.</p>
  </div>
  <div class="btn btn-orange" style="left:139px;top:4652px;width:228px;height:42px">Kontakt aufnehmen</div>
  <div class="photo" role="img" aria-label="Porträtfoto des Coaches mit verschränkten Armen" style="left:722px;top:4266px;width:330px;height:330px;border-radius:50%;background:linear-gradient(135deg,#e6ecf1,#b3c8da 55%,#f1f3f5)"></div>
  <div class="abs" style="left:722px;width:330px;top:4625px;text-align:center;font-size:18px;font-weight:600;color:var(--ink)">Stefan Brandauer</div>
  <div class="abs" style="left:722px;width:330px;top:4660px;text-align:center;font-size:16px;letter-spacing:3px;color:var(--blue-dark)">KLARWERK COACHING</div>
</section>

<!-- Footer -->
<footer class="footer">
  <div class="abs" style="left:0;width:1200px;top:50px;font-size:16px;font-weight:600">Impressum&nbsp;&nbsp;&nbsp;Datenschutz</div>
  <div class="abs" style="left:0;width:1200px;top:104px;font-size:14px">© 2024 Stefan Brandauer Coaching</div>
</footer>

</body>
</html>
```